New Company Business Card Design

I have a new company logo and I want a new business card design. I dont know if the logo file i attached is in the correct format or quality. We are a New York City Specialty construction Firm specializing in high risk out of the box projects. I want a simple and classy business card that people will his card is as crisp as the work his company does.

Target Market(s)

Clients in the heavy construction industry in New York City

Industry/Entity Type

Construction Company

Contact Information for Business Card

Simple Classy - DIFFERENT

Font styles to use
Other font styles liked:
• Mach the logo font in some way

Colors

Designer to choose colors to be used in the design.

Requirements
Must have
• Uniqueness
Nice to have
• Nothing particular - Just different and classy - Timeless
Should not have
• Goofy Shit or Gimmicky shit

```html
<!DOCTYPE html>
<html lang="en">
<head>
<meta charset="utf-8">
<title>Tervo Builders – Business Card</title>
<link rel="stylesheet" href="https://fonts.googleapis.com/css2?family=Open+Sans:wght@700;800&display=swap">
<style>
  :root {
    --brand-blue: #1b4a9b;
    --stripe-blue: #0f4c98;
    --ink: #111111;
    --paper: #ffffff;
    --edge: #3a5f9e;
  }
  html, body {
    margin: 0;
    width: 1200px;
    height: 1000px;
    overflow: hidden;
    background: var(--paper);
    font-family: "Open Sans", Arial, sans-serif;
  }
  .canvas { position: relative; width: 1200px; height: 1000px; }

  .card {
    position: absolute;
    left: 239px;
    width: 687px;
    background: var(--paper);
    overflow: hidden;
    box-sizing: border-box;
  }
  .card--back { top: 34px; height: 389px; border: 1px solid var(--edge); }
  .card--front { top: 543px; height: 392px; border-left: 1px solid #9aa; border-right: 1px solid #9aa; }

  .band { position: absolute; left: 0; right: 0; background: var(--brand-blue); }

  .wordmark {
    position: absolute;
    left: 0; right: 0;
    text-align: center;
    color: var(--brand-blue);
    font-weight: 800;
    line-height: 1;
  }
  .wordmark__name { display: block; letter-spacing: 3px; }
  .wordmark__sub { display: block; letter-spacing: 6px; }

  .card--back .wordmark { top: 58px; }
  .card--back .wordmark__name { font-size: 76px; }
  .card--back .wordmark__sub { font-size: 19px; margin-top: 10px; }

  .card--front .wordmark { top: 112px; }
  .card--front .wordmark__name { font-size: 68px; }
  .card--front .wordmark__sub { font-size: 17px; margin-top: 9px; }

  .contact-strip { position: absolute; left: 0; top: 0; }
  .contact-text {
    font-family: "Open Sans", Arial, sans-serif;
    font-weight: 700;
    font-size: 16px;
    fill: var(--ink);
  }
  .contact-text--address { font-size: 13.5px; }
  .stripe { fill: var(--stripe-blue); }
  .icon { fill: none; stroke: var(--brand-blue); stroke-width: 1.4; }
  .icon--solid { fill: var(--brand-blue); stroke: none; }

  .holder {
    position: absolute;
    top: 258px;
    left: 0; right: 0;
    text-align: center;
    font-weight: 700;
    font-size: 19px;
    color: var(--ink);
  }
  .holder__rule {
    display: block;
    width: 180px;
    height: 2px;
    margin: 4px auto 0;
    background: linear-gradient(90deg, transparent, var(--ink) 20%, var(--ink) 80%, transparent);
  }
</style>
</head>
<body>
<div class="canvas">

  <section class="card card--back">
    <div class="wordmark">
      <span class="wordmark__name">TERVO</span>
      <span class="wordmark__sub">BUILDERS, INC.</span>
    </div>
    <div class="band" style="top:165px;height:62px;"></div>

    <svg class="contact-strip" width="687" height="389" viewBox="239 34 687 389">
      <g class="stripes">
        <polygon class="stripe" points="241,423 263,423 380,262 358,262"/>
        <polygon class="stripe" points="350,423 372,423 489,262 467,262"/>
        <polygon class="stripe" points="458,423 480,423 597,262 575,262"/>
        <polygon class="stripe" points="567,423 589,423 706,262 684,262"/>
        <polygon class="stripe" points="676,423 698,423 815,262 793,262"/>
        <polygon class="stripe" points="784,423 806,423 923,262 901,262"/>
      </g>

      <g class="icons">
        <g class="icon">
          <circle cx="411" cy="281" r="12"/>
          <ellipse cx="411" cy="281" rx="5" ry="12"/>
          <line x1="399" y1="281" x2="423" y2="281"/>
          <line x1="401" y1="275" x2="421" y2="275"/>
          <line x1="401" y1="287" x2="421" y2="287"/>
        </g>
        <path class="icon--solid" d="M515 268c2-1 4 0 5 2l2 4c1 2 0 3-1 4l-1 1c1 3 3 6 6 8l1-1c1-1 3-1 4 0l3 3c1 1 1 3 0 4l-2 2c-2 1-5 1-8-2-5-4-9-10-10-16 0-4 0-7 1-9z"/>
        <g class="icon">
          <path d="M628 296c-6-7-9-11-9-15a9 9 0 0 1 18 0c0 4-3 8-9 15z"/>
          <circle cx="628" cy="281" r="4"/>
        </g>
        <g>
          <rect class="icon--solid" x="730" y="271" width="17" height="26" rx="4"/>
          <rect x="733" y="276" width="11" height="7" fill="#ffffff"/>
          <rect class="icon--solid" x="733" y="267" width="2" height="5"/>
        </g>
        <g class="icon">
          <rect x="834" y="272" width="30" height="17"/>
          <polyline points="834,272 849,283 864,272"/>
        </g>
      </g>

      <g class="contacts">
        <text class="contact-text" text-anchor="middle" transform="translate(362 357) rotate(-54)">WWW.TERVO.COM</text>
        <text class="contact-text" text-anchor="middle" transform="translate(465 360) rotate(-54)">555-014-2290</text>
        <text class="contact-text contact-text--address" text-anchor="middle" transform="translate(566 348) rotate(-54)">
          <tspan x="0" dy="-14">118 Harbor Line Road -</tspan>
          <tspan x="0" dy="16">Eastport,</tspan>
          <tspan x="0" dy="16">New Jersey 07999</tspan>
        </text>
        <text class="contact-text" text-anchor="middle" transform="translate(686 360) rotate(-54)">555-017-4438</text>
        <text class="contact-text" text-anchor="middle" transform="translate(795 358) rotate(-54)">MT@TERVO.COM</text>
      </g>
    </svg>
  </section>

  <section class="card card--front">
    <div class="band" style="top:0;height:62px;"></div>
    <div class="wordmark">
      <span class="wordmark__name">TERVO</span>
      <span class="wordmark__sub">BUILDERS, INC.</span>
    </div>
    <div class="holder">
      Marcus T. Ellery
      <span class="holder__rule"></span>
    </div>
    <div class="band" style="top:329px;height:63px;"></div>
  </section>

</div>
</body>
</html>
```